Bref créative
BRFinishing Co.
NYC | Westchester |
Simple
Darrel Hutchins Jr
Project Manager
8 Lowell Terrace
Cold Meadow, NY 10488
brfinishinginfo@brfmail-example.com
We'd like to see ideas for vertical card designs as well.
It's all in the finish
Logo
logo

```html
<!DOCTYPE html>
<html lang="en">
<head>
<meta charset="utf-8">
<title>BRFinishing Co. — Vertical Business Card</title>
<link href="https://fonts.googleapis.com/css2?family=Arimo:wght@400;700&display=swap" rel="stylesheet">
<style>
  :root {
    --page: #ffffff;
    --card-light: #fbfbfb;
    --card-shade: #e9e9e9;
    --ink: #1c1c1c;
    --ink-soft: #2b2b2b;
    --bar-dark: #3a3a3a;
    --bar-mid: #8a8a8a;
    --bar-light: #d6d6d6;
    --brand-dot: #2f2f2f;
  }
  * { margin: 0; padding: 0; box-sizing: border-box; }
  html, body {
    width: 1200px;
    height: 1009px;
    overflow: hidden;
    background: var(--page);
    font-family: "Arimo", Arial, sans-serif;
    color: var(--ink);
  }
  .sheet {
    position: relative;
    width: 1200px;
    height: 1009px;
  }
  .card {
    position: absolute;
    top: 0;
    width: 566px;
    height: 1009px;
    background: radial-gradient(ellipse at 50% 40%, var(--card-light) 0%, #f3f3f3 55%, var(--card-shade) 100%);
    box-shadow: 0 0 4px rgba(0,0,0,0.15);
    overflow: hidden;
  }
  .card--front { left: 14px; }
  .card--back { left: 622px; }

  .metal-bar {
    position: absolute;
    left: 0;
    width: 100%;
    height: 58px;
    background: linear-gradient(90deg, var(--bar-dark) 0%, var(--bar-mid) 8%, var(--bar-light) 30%, #f2f2f2 50%, var(--bar-light) 70%, var(--bar-mid) 92%, var(--bar-dark) 100%);
  }
  .metal-bar::after {
    content: "";
    position: absolute;
    left: 0; right: 0;
    height: 14px;
    background: linear-gradient(180deg, rgba(0,0,0,0.45), rgba(0,0,0,0));
  }
  .metal-bar--top { top: 0; }
  .metal-bar--top::after { top: 44px; background: linear-gradient(180deg, rgba(0,0,0,0), rgba(0,0,0,0.35)); }
  .metal-bar--bottom { bottom: 0; }
  .metal-bar--bottom::after { top: 0; }

  .brand {
    position: absolute;
    top: 148px;
    left: 34px;
    display: flex;
    align-items: center;
    gap: 14px;
  }
  .brand__dot {
    width: 34px;
    height: 34px;
    border-radius: 50%;
    background: var(--brand-dot);
  }
  .brand__name {
    font-weight: 700;
    font-size: 52px;
    letter-spacing: -1px;
    color: var(--ink);
    line-height: 1;
  }

  .identity {
    position: absolute;
    top: 496px;
    left: 0;
    width: 100%;
    text-align: center;
  }
  .identity__name {
    font-weight: 700;
    font-size: 27px;
    color: var(--ink);
  }
  .identity__role {
    margin-top: 8px;
    font-size: 25px;
    color: var(--ink-soft);
  }

  .contact {
    position: absolute;
    left: 28px;
    top: 838px;
    font-size: 22px;
    line-height: 28px;
    color: var(--ink-soft);
  }
</style>
</head>
<body>
  <main class="sheet">
    <section class="card card--front">
      <div class="metal-bar metal-bar--top"></div>
      <div class="brand">
        <span class="brand__dot"></span>
        <span class="brand__name">BRFinishing Co.</span>
      </div>
      <div class="identity">
        <p class="identity__name">Darrel Hutchins Jr</p>
        <p class="identity__role">Project Manager</p>
      </div>
      <address class="contact" style="font-style: normal;">
        8 Lowell Terrace<br>
        Cold Meadow, NY 10488<br>
        Phone : 347.555.0192<br>
        Email : brfinishinginfo@brfmail-example.com
      </address>
      <div class="metal-bar metal-bar--bottom"></div>
    </section>

    <section class="card card--back">
      <div class="metal-bar metal-bar--top"></div>
      <div class="brand">
        <span class="brand__dot"></span>
        <span class="brand__name">BRFinishing Co.</span>
      </div>
      <div class="metal-bar metal-bar--bottom"></div>
    </section>
  </main>
</body>
</html>
```